Pet business needs a business card

Pet shop needs a business card. Like dark background and and debased look.

Hedgerowpups
Lindelaan 27
B - 3270 Korbeek
Belgium

www.hedgerowpups.example
mail@hedgerowpups.example
Phone +32471869203

I will ad a tagline shortly.

Industry/Entity Type

Shop

Font styles to use
Sans Serif

Requirements
Must have
• Must be possible to print the card debased. See example image.

```html
<!DOCTYPE html>
<html lang="en">
<head>
<meta charset="utf-8">
<title>Hedgerowpups business card</title>
<link href="https://fonts.googleapis.com/css2?family=Roboto+Condensed:wght@400;700&display=swap" rel="stylesheet">
<style>
  :root {
    --backdrop: #e6e6e3;
    --card: #2d323a;
    --accent: #f2a23a;
    --ink-light: #c9cbcf;
    --ink-muted: #8e9299;
    --phone: #e9e6df;
  }
  * { margin: 0; padding: 0; box-sizing: border-box; }
  html, body { width: 1200px; height: 885px; overflow: hidden; }
  body {
    background: var(--backdrop);
    font-family: "Roboto Condensed", Arial, sans-serif;
    position: relative;
  }
  .card {
    position: absolute;
    top: 274px;
    width: 520px;
    height: 336px;
    background: var(--card);
    overflow: hidden;
    box-shadow: 0 6px 18px rgba(0,0,0,0.18);
  }
  .card--front { left: 50px; }
  .card--back { left: 630px; }

  .card__accent-shape {
    position: absolute;
    left: 0; top: 0;
    width: 520px; height: 336px;
  }
  .brand-name {
    position: absolute;
    font-weight: 700;
    letter-spacing: -0.5px;
    color: var(--accent);
    text-transform: lowercase;
  }
  .card--front .brand-name {
    left: 34px; top: 58px;
    font-size: 34px;
  }
  .address {
    position: absolute;
    left: 34px; top: 196px;
    font-size: 11px;
    line-height: 15px;
    color: var(--ink-muted);
    letter-spacing: 0.4px;
  }
  .web {
    position: absolute;
    left: 34px; top: 276px;
    font-size: 11px;
    line-height: 15px;
    color: var(--ink-muted);
    letter-spacing: 0.4px;
  }
  .phone {
    position: absolute;
    left: 300px; top: 148px;
    color: var(--phone);
  }
  .phone__label {
    display: block;
    font-size: 14px;
    color: var(--ink-muted);
    margin-bottom: 2px;
  }
  .phone__number {
    font-size: 27px;
    letter-spacing: 0.5px;
  }

  .card--back .brand-lockup {
    position: absolute;
    left: 0; top: 0; width: 100%; height: 100%;
    display: flex;
    align-items: center;
    justify-content: center;
    gap: 14px;
  }
  .card--back .brand-mark {
    width: 22px; height: 22px;
    border-radius: 50%;
    background: var(--accent);
  }
  .card--back .brand-name {
    position: static;
    font-size: 44px;
  }
</style>
</head>
<body>
  <section class="card card--front" aria-label="Card front">
    <svg class="card__accent-shape" viewBox="0 0 520 336" aria-hidden="true">
      <path d="M520 70 C 410 80, 300 150, 262 336 L 520 336 Z" fill="var(--accent)"/>
    </svg>
    <div class="brand-name">hedgerowpups</div>
    <p class="address">Lindelaan 27<br>B - 3270 Korbeek<br>Belgium</p>
    <p class="web">www.hedgerowpups.example<br>mail@hedgerowpups.example</p>
    <p class="phone"><span class="phone__label">Phone</span><span class="phone__number">+32471869203</span></p>
  </section>

  <section class="card card--back" aria-label="Card back">
    <div class="brand-lockup">
      <span class="brand-mark" aria-hidden="true"></span>
      <span class="brand-name">hedgerowpups</span>
    </div>
  </section>
</body>
</html>
```